Pageloom Website Update - Blockwright

I'm currently using Blockwright and would like my site to be updated. A nice facelift to the current pages. We are a small boutique animation service company.
I have a list of similar production houses to use as references and would like the format/style of the site not to feel so corporate and infuse the fun that we bring to working with clients on animated projects.

Additionally, I'd like to add 2 more pages focusing on more portfolio work and Original IP - which is now our primary goal to sell our show ideas. Maybe have a password projected behind an image showcasing the show/ film. Go to our current site to review. www.tallmoosestudio.example

Target Market(s)

Animation/ Commercials/ Vistora/ Quorvex/ Plumtree/ KTV - Okay with first page being shorter and not as long as well. Have contact us 'above the fold' on options as well.

Industry/Entity Type

Animation and Film

Coding

Requirements
Must have
• Current 3 pages - additional 2 - we can focus on layout and arrangement with temporary images then swap with real assets when ready.
Nice to have
• site examples: fernleafworks.example, Mirelo Barn, Wuvel Studios, Quillfern.example, Brightkettle Animation, Windlatch Animation Studios, ZeZo Studios use Orvane Max as inspiration.

```html
<!DOCTYPE html>
<html lang="en">
<head>
<meta charset="utf-8">
<title>Tall Moose Studio – Homepage Layouts</title>
<link href="https://fonts.googleapis.com/css2?family=Oswald:wght@500;600&family=Roboto:wght@400;500;700&display=swap" rel="stylesheet">
<style>
:root{
  --stage:#cfd0d3;
  --ink:#14131f;
  --footer:#09090c;
  --purple:#5a2ad8;
  --purple-deep:#4a17c9;
  --violet-a:#7a55f0;
  --violet-b:#4512c4;
  --red:#e5093f;
  --white:#ffffff;
  --muted:#cfcde0;
}
*{margin:0;padding:0;box-sizing:border-box}
html,body{width:770px;height:1200px;overflow:hidden;background:var(--stage)}
body{position:relative;font-family:"Roboto",Arial,sans-serif;color:var(--white)}
.page{position:absolute;background:var(--ink);overflow:hidden}
.page--wide{left:45px;top:78px;width:308px;height:958px}
.page--slider{left:395px;top:78px;width:330px;height:1044px}
.abs{position:absolute}
.brand{font-family:"Oswald",sans-serif;font-weight:600;color:var(--purple);letter-spacing:.3px;white-space:nowrap}
.nav{top:0;left:0;right:0;height:20px;background:var(--ink)}
.nav__brand{top:4px;font-size:9px;line-height:12px}
.nav__links{top:8px;display:flex;gap:7px;font-size:3.6px;font-weight:500;white-space:nowrap}
.social{display:flex;gap:3px}
.social span{width:9px;height:9px;border-radius:50%;background:var(--purple)}
.hero{top:20px;left:0;right:0;display:flex;gap:3px}
.hero__panel{flex:1}
.arrow{width:22px;height:22px;border-radius:50%;background:var(--white);display:flex;align-items:center;justify-content:center}
.video{border-radius:1px;display:flex;align-items:center;justify-content:center}
.play{width:17px;height:12px;border-radius:3px;background:#ff0000;display:flex;align-items:center;justify-content:center}
.feature__icon{width:15px;height:15px;border-radius:50%;background:radial-gradient(circle at 40% 35%,#2fa3ff,#2034b8)}
.feature__title{font-family:"Oswald",sans-serif;font-weight:500;font-size:10.5px;line-height:12px;color:var(--purple);white-space:nowrap}
.feature__text{font-size:3.5px;line-height:5.2px;color:var(--muted);width:112px}
.btn{height:12px;padding:0 8px;border-radius:6px;background:var(--red);display:flex;align-items:center;gap:3px;font-size:3.8px;font-weight:700;white-space:nowrap}
.btn i{width:4px;height:4px;border-radius:50%;background:var(--white);display:inline-block}
.band{top:441px;left:0;right:0;height:75px;background:linear-gradient(100deg,var(--violet-a),var(--violet-b))}
.band__eyebrow{font-size:3.8px;font-weight:700;white-space:nowrap}
.band__title{font-family:"Oswald",sans-serif;font-weight:500;font-size:8.6px;line-height:11px;white-space:nowrap}
.section-title{font-family:"Oswald",sans-serif;font-weight:500;font-size:9.5px;text-align:center;left:0;right:0;white-space:nowrap}
.section-title--purple{color:var(--purple)}
.grid{display:grid;grid-template-columns:repeat(4,66px);grid-auto-rows:53px;gap:6px 5px}
.expertise{left:0;right:0;height:170px;background:linear-gradient(110deg,var(--violet-a),var(--violet-b) 80%)}
.skill{width:72px}
.skill--left{text-align:right}
.skill h4{font-size:4.6px;font-weight:700;line-height:6px}
.skill p{font-size:3.1px;line-height:5px;color:#e6e0ff}
.skill-icon{width:20px;height:20px;border-radius:50%;background:var(--white);display:flex;align-items:center;justify-content:center}
.footer{left:0;right:0;height:89px;background:var(--footer);text-align:center}
.footer__brand{left:0;right:0;font-size:12px;line-height:14px}
.footer__links{left:0;right:0;display:flex;justify-content:center;gap:6px;font-size:3.6px;font-weight:700;white-space:nowrap}
.footer__links em{font-style:normal;color:#aaa}
.footer__copy{left:0;right:0;font-size:3.5px;color:#ddd}
.footer__copy u{color:var(--white)}
.footer__social{left:0;right:0;display:flex;justify-content:center;gap:3px}
.footer__social span{width:11px;height:11px;border-radius:50%;background:#e9e9ee}
.footer__social span:first-child{background:var(--purple)}
.card{top:703px;height:78px;width:102px;background:var(--red);text-align:center;padding-top:24px}
.card h5{font-family:"Oswald",sans-serif;font-weight:500;font-size:7px;line-height:9px}
.card hr{width:14px;border:0;border-top:1px solid var(--white);margin:3px auto 6px}
.card p{font-size:3.6px;line-height:6px}
.card .dots{display:flex;justify-content:center;gap:4px;margin-top:2px}
.card .dots span{width:4px;height:4px;border-radius:50%;background:var(--white)}
</style>
</head>
<body>

<!-- Layout A: four-panel hero -->
<section class="page page--wide">
  <header class="abs nav">
    <div class="abs brand nav__brand" style="left:28px">TALL MOOSE</div>
    <nav class="abs nav__links" style="left:110px"><span>Home</span><span>About Us</span><span>Team</span><span>Projects</span><span>Careers</span><span>Contact Us</span></nav>
    <div class="abs social" style="left:247px;top:5px"><span></span><span></span><span></span></div>
  </header>
  <div class="abs hero" style="height:156px">
    <div class="hero__panel" role="img" aria-label="Illustrated forest scene with cartoon characters" style="background:linear-gradient(160deg,#c8703f,#6f8f3a 70%,#dfe6e6)"></div>
    <div class="hero__panel" role="img" aria-label="3D animated giraffe character in glasses" style="background:linear-gradient(180deg,#7d8488,#6b5230 55%,#9c7a45)"></div>
    <div class="hero__panel" role="img" aria-label="Night fantasy ship and castle painting" style="background:linear-gradient(180deg,#2b2aa0,#3a49c8 50%,#14136a)"></div>
    <div class="hero__panel" role="img" aria-label="Underwater scene with diver and fish" style="background:linear-gradient(180deg,#2f8fd8,#1663c2 60%,#0b2e6a)"></div>
  </div>

  <div class="abs video" role="img" aria-label="Animation reel video still with puppy character" style="left:28px;top:204px;width:126px;height:82px;background:linear-gradient(120deg,#6d4be0,#2a1680 70%,#1a0f4a)"><div class="play"><svg width="6" height="6" viewBox="0 0 6 6"><path d="M1 0l5 3-5 3z" fill="#fff"/></svg></div></div>
  <div class="abs feature__icon" style="left:172px;top:215px"></div>
  <div class="abs feature__title" style="left:172px;top:235px">ANIMATION REEL</div>
  <div class="abs feature__text" style="left:172px;top:250px">Story and Animation is where TMS thrives.</div>
  <div class="abs btn" style="left:172px;top:264px">LEARN MORE <i></i></div>

  <div class="abs feature__icon" style="left:28px;top:324px"></div>
  <div class="abs feature__title" style="left:28px;top:344px">GIRAFFES &amp; KIDS ARE FREE!</div>
  <div class="abs feature__text" style="left:28px;top:362px">Tall Moose kicked major butt on this fun project. Read more about the role we played bringing this commercial to life...</div>
  <div class="abs btn" style="left:28px;top:379px">LEARN MORE <i></i></div>
  <div class="abs video" role="img" aria-label="Commercial video still with giraffe beside a painting" style="left:154px;top:316px;width:125px;height:82px;background:linear-gradient(180deg,#9aa0a4,#6a5a48 55%,#cfcfcf)"><div class="play"><svg width="6" height="6" viewBox="0 0 6 6"><path d="M1 0l5 3-5 3z" fill="#fff"/></svg></div></div>

  <div class="abs band">
    <div class="abs band__eyebrow" style="left:129px;top:16px">Dream Big, Stand Tall!</div>
    <div class="abs band__title" style="left:129px;top:22px">WHEN IS NOW A GOOD TIME TO WRITE?</div>
    <div class="abs btn" style="left:129px;top:42px">LEARN MORE <i></i></div>
  </div>
  <div class="abs" role="img" aria-label="Green one-eyed monster mascot" style="left:35px;top:417px;width:76px;height:90px;border-radius:40% 40% 35% 35%;background:radial-gradient(circle at 50% 45%,#9de04a,#4d9a1c)"></div>

  <h2 class="abs section-title section-title--purple" style="top:538px">OUR PROJECTS</h2>
  <div class="abs grid" style="left:15px;top:559px">
    <div role="img" aria-label="Project: 3D town street" style="background:linear-gradient(180deg,#8ec4ea,#7e9a5a)"></div>
    <div role="img" aria-label="Project: festive slot game" style="background:linear-gradient(160deg,#c0302a,#e7a43a)"></div>
    <div role="img" aria-label="Project: city sketch storyboard" style="background:linear-gradient(180deg,#e6e6e6,#8c8c8c)"></div>
    <div role="img" aria-label="Project: mascot video with presenter" style="background:linear-gradient(120deg,#6b4a35,#2b2320)"></div>
    <div role="img" aria-label="Project: illustrated character guide" style="background:linear-gradient(160deg,#c47a45,#5e8a3e)"></div>
    <div role="img" aria-label="Project: desert landscape animation" style="background:linear-gradient(180deg,#b0706a,#6a3a35)"></div>
    <div role="img" aria-label="Project: presenter with mascots" style="background:linear-gradient(180deg,#b7a89c,#3c3636)"></div>
    <div role="img" aria-label="Project: parade event with mascot" style="background:linear-gradient(180deg,#7aa4d4,#4e6a8a)"></div>
  </div>

  <div class="abs expertise" style="top:699px">
    <h2 class="abs section-title" style="top:12px">OUR EXPERTISE</h2>
    <div class="abs skill skill--left" style="left:11px;top:45px"><h4>IP CREATION</h4><p>Developing, Directing and Selling captivating stories is in our DNA. Check what we are cooking up.</p></div>
    <div class="abs skill skill--left" style="left:11px;top:84px"><h4>STORY</h4><p>From Storyboarding, to Story Consulting, and Script Doctoring, TM turns your stories into attention making monsters!</p></div>
    <div class="abs skill skill--left" style="left:11px;top:123px"><h4>ANIMATION</h4><p>Pound for Pound we have worlds best animators and pride ourselves on the quality level we deliver.</p></div>
    <div class="abs skill-icon" style="left:90px;top:46px"></div>
    <div class="abs skill-icon" style="left:90px;top:84px"></div>
    <div class="abs skill-icon" style="left:90px;top:123px"></div>
    <div class="abs" role="img" aria-label="Purple furry one-eyed monster mascot" style="left:120px;top:43px;width:65px;height:100px;border-radius:45% 45% 30% 30%;background:radial-gradient(circle at 50% 45%,#a58bff,#5a36d8)"></div>
    <div class="abs skill-icon" style="left:194px;top:46px"></div>
    <div class="abs skill-icon" style="left:194px;top:84px"></div>
    <div class="abs skill-icon" style="left:194px;top:123px"></div>
    <div class="abs skill" style="left:220px;top:47px"><h4>3D RIGGING</h4><p>Creating Feature level robust rigs to game and real time rigs with dynamics.</p></div>
    <div class="abs skill" style="left:220px;top:86px"><h4>CHARACTER DESIGN</h4><p>Designing premier characters from concept to finished packets for 3D Development.</p></div>
    <div class="abs skill" style="left:220px;top:124px"><h4>VIS DEV</h4><p>Building worlds and settings to enrich the places characters play. Saying more with an image.</p></div>
  </div>

  <footer class="abs footer" style="top:869px">
    <div class="abs brand footer__brand" style="top:16px">TALL MOOSE</div>
    <nav class="abs footer__links" style="top:35px"><span>HOME</span><em>/</em><span>ABOUT US</span><em>/</em><span>TEAM</span><em>/</em><span>PROJECTS</span><em>/</em><span>CAREERS</span><em>/</em><span>CONTACT US</span></nav>
    <p class="abs footer__copy" style="top:45px">Copyright© 2022 <u>tallmoosestudio</u> | All Rights Reserved</p>
    <div class="abs footer__social" style="top:58px"><span></span><span></span><span></span><span></span></div>
  </footer>
</section>

<!-- Layout B: slider hero with contact cards -->
<section class="page page--slider">
  <header class="abs nav">
    <nav class="abs nav__links" style="left:40px"><span>Home</span><span>About Us</span><span>Team</span><span>Projects</span></nav>
    <div class="abs brand nav__brand" style="left:140px">TALL MOOSE</div>
    <nav class="abs nav__links" style="left:205px"><span>Careers</span><span>Contact Us</span></nav>
    <div class="abs social" style="left:258px;top:5px"><span></span><span></span><span></span></div>
  </header>
  <div class="abs hero" style="height:144px">
    <div class="hero__panel" role="img" aria-label="Illustrated forest scene with cartoon characters" style="background:linear-gradient(160deg,#c8703f,#6f8f3a 70%,#dfe6e6)"></div>
    <div class="hero__panel" role="img" aria-label="3D animated child with a drum" style="background:linear-gradient(180deg,#3a5a3a,#d83a3a 55%,#3a5a9a)"></div>
    <div class="hero__panel" role="img" aria-label="3D animated giraffe character in glasses" style="background:linear-gradient(180deg,#7d8488,#6b5230 55%,#9c7a45)"></div>
    <div class="hero__panel" role="img" aria-label="Stage scene with puppy and girl characters" style="background:linear-gradient(180deg,#8a4ef0,#3a2a7a 60%,#2a2222)"></div>
    <div class="hero__panel" role="img" aria-label="Underwater scene with diver and fish" style="background:linear-gradient(180deg,#2f8fd8,#1663c2 60%,#0b2e6a)"></div>
  </div>
  <div class="abs arrow" style="left:-2px;top:81px"><svg width="6" height="8" viewBox="0 0 6 8"><path d="M5 0L1 4l4 4" stroke="#14131f" fill="none" stroke-width="1.2"/></svg></div>
  <div class="abs arrow" style="left:310px;top:81px"><svg width="6" height="8" viewBox="0 0 6 8"><path d="M1 0l4 4-4 4" stroke="#14131f" fill="none" stroke-width="1.2"/></svg></div>

  <div class="abs video" role="img" aria-label="Animation reel video still with puppy character" style="left:39px;top:204px;width:126px;height:82px;background:linear-gradient(120deg,#6d4be0,#2a1680 70%,#1a0f4a)"><div class="play"><svg width="6" height="6" viewBox="0 0 6 6"><path d="M1 0l5 3-5 3z" fill="#fff"/></svg></div></div>
  <div class="abs feature__icon" style="left:182px;top:215px"></div>
  <div class="abs feature__title" style="left:182px;top:235px">ANIMATION REEL</div>
  <div class="abs feature__text" style="left:182px;top:250px">Story and Animation is where TMS thrives.</div>
  <div class="abs btn" style="left:182px;top:264px">LEARN MORE <i></i></div>

  <div class="abs feature__icon" style="left:39px;top:324px"></div>
  <div class="abs feature__title" style="left:39px;top:344px">GIRAFFES &amp; KIDS ARE FREE!</div>
  <div class="abs feature__text" style="left:39px;top:362px">Tall Moose kicked major butt on this fun project. Read more about the role we played bringing this commercial to life...</div>
  <div class="abs btn" style="left:39px;top:379px">LEARN MORE <i></i></div>
  <div class="abs video" role="img" aria-label="Commercial video still with giraffe beside a painting" style="left:165px;top:316px;width:125px;height:82px;background:linear-gradient(180deg,#9aa0a4,#6a5a48 55%,#cfcfcf)"><div class="play"><svg width="6" height="6" viewBox="0 0 6 6"><path d="M1 0l5 3-5 3z" fill="#fff"/></svg></div></div>

  <div class="abs band">
    <div class="abs band__eyebrow" style="left:140px;top:16px">Dream Big, Stand Tall!</div>
    <div class="abs band__title" style="left:140px;top:22px">WHEN IS NOW A GOOD TIME TO WRITE?</div>
    <div class="abs btn" style="left:140px;top:42px">LEARN MORE <i></i></div>
  </div>
  <div class="abs" role="img" aria-label="Green one-eyed monster mascot" style="left:40px;top:417px;width:76px;height:90px;border-radius:40% 40% 35% 35%;background:radial-gradient(circle at 50% 45%,#9de04a,#4d9a1c)"></div>

  <h2 class="abs section-title section-title--purple" style="top:538px">OUR PROJECTS</h2>
  <div class="abs grid" style="left:26px;top:559px">
    <div role="img" aria-label="Project: 3D town street" style="background:linear-gradient(180deg,#8ec4ea,#7e9a5a)"></div>
    <div role="img" aria-label="Project: festive slot game" style="background:linear-gradient(160deg,#c0302a,#e7a43a)"></div>
    <div role="img" aria-label="Project: city sketch storyboard" style="background:linear-gradient(180deg,#e6e6e6,#8c8c8c)"></div>
    <div role="img" aria-label="Project: mascot video with presenter" style="background:linear-gradient(120deg,#6b4a35,#2b2320)"></div>
    <div role="img" aria-label="Project: illustrated character guide" style="background:linear-gradient(160deg,#c47a45,#5e8a3e)"></div>
    <div role="img" aria-label="Project: desert landscape animation" style="background:linear-gradient(180deg,#b0706a,#6a3a35)"></div>
    <div role="img" aria-label="Project: presenter with mascots" style="background:linear-gradient(180deg,#b7a89c,#3c3636)"></div>
    <div role="img" aria-label="Project: parade event with mascot" style="background:linear-gradient(180deg,#7aa4d4,#4e6a8a)"></div>
  </div>

  <div class="abs card" style="left:6px"><h5>CONTACT</h5><hr><p>hello@tallmoosestudio.example<br>+1 (555) 010-0199</p></div>
  <div class="abs card" style="left:114px"><h5>VISIT</h5><hr><p>123, Lorem ipsum dolor sit amet,<br>consectetur adipiscing elit,</p></div>
  <div class="abs card" style="left:222px;padding-top:27px"><h5>SOCIALIZE</h5><hr><div class="dots"><span></span><span></span><span></span><span></span><span></span></div></div>

  <div class="abs expertise" style="top:787px">
    <h2 class="abs section-title" style="top:12px">OUR EXPERTISE</h2>
    <div class="abs skill skill--left" style="left:23px;top:45px"><h4>IP CREATION</h4><p>Developing, Directing and Selling captivating stories is in our DNA. Check what we are cooking up.</p></div>
    <div class="abs skill skill--left" style="left:23px;top:84px"><h4>STORY</h4><p>From Storyboarding, to Story Consulting, and Script Doctoring, TM turns your stories into attention making monsters!</p></div>
    <div class="abs skill skill--left" style="left:23px;top:123px"><h4>ANIMATION</h4><p>Pound for Pound we have worlds best animators and pride ourselves on the quality level we deliver.</p></div>
    <div class="abs skill-icon" style="left:102px;top:46px"></div>
    <div class="abs skill-icon" style="left:102px;top:84px"></div>
    <div class="abs skill-icon" style="left:102px;top:123px"></div>
    <div class="abs" role="img" aria-label="Purple furry one-eyed monster mascot" style="left:131px;top:43px;width:66px;height:100px;border-radius:45% 45% 30% 30%;background:radial-gradient(circle at 50% 45%,#a58bff,#5a36d8)"></div>
    <div class="abs skill-icon" style="left:205px;top:46px"></div>
    <div class="abs skill-icon" style="left:205px;top:84px"></div>
    <div class="abs skill-icon" style="left:205px;top:123px"></div>
    <div class="abs skill" style="left:231px;top:47px"><h4>3D RIGGING</h4><p>Creating Feature level robust rigs to game and real time rigs with dynamics.</p></div>
    <div class="abs skill" style="left:231px;top:86px"><h4>CHARACTER DESIGN</h4><p>Designing premier characters from concept to finished packets for 3D Development.</p></div>
    <div class="abs skill" style="left:231px;top:124px"><h4>VIS DEV</h4><p>Building worlds and settings to enrich the places characters play. Saying more with an image.</p></div>
  </div>

  <footer class="abs footer" style="top:956px;height:88px">
    <div class="abs brand footer__brand" style="top:16px">TALL MOOSE</div>
    <nav class="abs footer__links" style="top:35px"><span>HOME</span><em>/</em><span>ABOUT US</span><em>/</em><span>TEAM</span><em>/</em><span>PROJECTS</span><em>/</em><span>CAREERS</span><em>/</em><span>CONTACT US</span></nav>
    <p class="abs footer__copy" style="top:45px">Copyright© 2022 <u>tallmoosestudio</u> | All Rights Reserved</p>
    <div class="abs footer__social" style="top:58px"><span></span><span></span><span></span><span></span></div>
  </footer>
</section>

</body>
</html>
```